1300 Gearbloom Van wrap

We are forklift mechanics.
Design a simple wrap to suit our 4 vans with our logo.
Add some colour/design using the base colours happy to add other colours as suits and highlights/shadows to balance/break up the white but not over power it.
Include mobile number 0491 572 608

```html
<!DOCTYPE html>
<html lang="en">
<head>
<meta charset="utf-8">
<title>1300 Gearbloom – Van Wrap</title>
<link rel="stylesheet" href="https://fonts.googleapis.com/css2?family=Oswald:wght@600;700&family=Open+Sans:wght@600&display=swap">
<style>
  :root {
    --backdrop: #f1f1f1;
    --wrap-white: #ffffff;
    --ink-black: #111111;
    --charcoal: #2a2a2a;
    --brand-red: #d0121b;
    --deep-red: #9e0c12;
    --text-white: #ffffff;
    --text-light: #ececec;
  }
  * { margin: 0; padding: 0; box-sizing: border-box; }
  html, body { width: 1200px; height: 900px; overflow: hidden; background: var(--backdrop); }
  .canvas { position: relative; width: 1200px; height: 900px; }
  .wrap-art { position: absolute; inset: 0; }
  .service-list {
    position: absolute; left: 70px; top: 236px; list-style: none;
    font-family: "Oswald", "Arial Narrow", sans-serif; font-weight: 700;
    font-size: 36px; line-height: 45px; letter-spacing: 1px; color: var(--text-light);
    text-transform: uppercase;
  }
  .service-list li::before {
    content: ""; display: inline-block; width: 15px; height: 15px; border-radius: 50%;
    background: var(--text-light); margin-right: 9px; vertical-align: middle; position: relative; top: -3px;
  }
  .brand-name {
    position: absolute; left: 470px; top: 392px;
    font-family: "Oswald", "Arial Narrow", sans-serif; font-weight: 700;
    font-size: 74px; line-height: 1; color: var(--brand-red); text-transform: uppercase;
    letter-spacing: -1px; white-space: nowrap;
  }
  .phone {
    position: absolute; left: 672px; top: 506px; display: flex; align-items: center; gap: 6px;
    font-family: "Oswald", "Arial Narrow", sans-serif; font-weight: 600;
    font-size: 27px; letter-spacing: 2px; color: var(--ink-black);
  }
  .phone-icon { width: 20px; height: 20px; fill: var(--ink-black); }
  .website {
    position: absolute; left: 386px; top: 584px; width: 470px; text-align: center;
    font-family: "Open Sans", Arial, sans-serif; font-weight: 600;
    font-size: 21px; letter-spacing: 4.3px; color: var(--text-light);
  }
</style>
</head>
<body>
<main class="canvas">
  <svg class="wrap-art" viewBox="0 0 1200 900" width="1200" height="900" aria-hidden="false">
    <defs>
      <linearGradient id="red-band-shade" x1="0" y1="0" x2="0" y2="1">
        <stop offset="0" stop-color="var(--brand-red)"/>
        <stop offset="1" stop-color="var(--deep-red)"/>
      </linearGradient>
      <linearGradient id="gear-tone" x1="0" y1="0" x2="1" y2="1">
        <stop offset="0" stop-color="#3a3a3a"/>
        <stop offset="0.5" stop-color="#8a8a8a"/>
        <stop offset="1" stop-color="#2a2a2a"/>
      </linearGradient>
    </defs>
    <!-- white wrap panel -->
    <rect class="wrap-panel" x="30" y="210" width="1140" height="400" rx="28" fill="var(--wrap-white)"/>
    <!-- black sweep, top left -->
    <path class="black-sweep" d="M30 238 Q30 210 60 210 L300 210 Q410 214 440 330 Q460 420 490 470 L30 470 Z" fill="var(--ink-black)"/>
    <!-- gear decoration area -->
    <path class="gear-area" role="img" aria-label="Large chrome gear decoration sweeping across the rear panel"
          d="M40 420 Q200 360 420 420 L480 470 Q300 440 40 470 Z" fill="url(#gear-tone)" opacity="0.85"/>
    <!-- red sweep, lower band -->
    <path class="red-sweep" d="M30 470 Q180 420 320 440 Q420 460 480 520 Q560 560 700 548 Q820 538 900 556 Q930 575 930 610 L58 610 Q30 610 30 582 Z" fill="url(#red-band-shade)"/>
  </svg>

  <ul class="service-list">
    <li>Hire</li>
    <li>Sales</li>
    <li>Service</li>
    <li>Repairs</li>
  </ul>

  <div class="brand-name">1300 Gearbloom</div>

  <div class="phone">
    <svg class="phone-icon" viewBox="0 0 24 24" aria-hidden="true">
      <path d="M6.6 10.8a15.1 15.1 0 0 0 6.6 6.6l2.2-2.2c.3-.3.7-.4 1-.2 1.1.4 2.3.6 3.6.6.6 0 1 .4 1 1V20c0 .6-.4 1-1 1A17 17 0 0 1 3 4c0-.6.4-1 1-1h3.5c.6 0 1 .4 1 1 0 1.3.2 2.5.6 3.6.1.3 0 .7-.2 1z"/>
    </svg>
    <span>0491 572 608</span>
  </div>

  <div class="website">www.1300gearbloom.com.au</div>
</main>
</body>
</html>
```